Website for Dental Office - The Bright Harbor Clinic

The bright harbor clinic is a dental office offering cosmetic dentistry, general dentistry, and multi-specialty dental care all under one roof in our state-of-the-art cosmetic dental center. We are particularly striving to provide services that fit the need of the young generation. Thus, we hope to have a modern, professional concise website that represents our spirit.

*Should be able to switch from English to Chinese

6 sections besides homepage:
Home, Meet us, Services,
Patient Info, Cases&Reviews, Blog, Contact

The Services sections should contain multiple subsections such as cleaning and prevention, cosmetic dentistry, implant dentistry, removable dentures, etc...
The Patient Info section is also intended to contain several subsections such as
New Patient offer, accepted Insurance, patient portal, helpful tips, etc...

Target Market(s)

young generation

Coding

Coded - Design and coding required

Number of Pages Required

5+ page

Font styles to use
Sans Serif

Colors
0592cd
33a6d7
85cae6
00a990
33b8a4
86cfc6
cee9f5
cfeae6
3277b5

Requirements
Must have
• *Should be able to switch from English to Chinese
Nice to have
• http://www.thebrightharborclinic.example/
• As a reference, the above link is the current website, but we would like to change the appearance and the content (our new logo's picture is attached)

```html
<!DOCTYPE html>
<html lang="en">
<head>
<meta charset="utf-8">
<title>The Bright Harbor Clinic – Dental Office</title>
<link href="https://fonts.googleapis.com/css2?family=Open+Sans:wght@400;600;700;800&display=swap" rel="stylesheet">
<style>
:root{
  --blue:#0592cd; --blue-mid:#33a6d7; --blue-soft:#85cae6; --blue-pale:#cee9f5; --blue-deep:#3277b5;
  --teal:#00a990; --teal-mid:#33b8a4; --teal-soft:#86cfc6; --teal-pale:#cfeae6;
  --ink:#1d1d1d; --grey:#6d6d6d; --line:#d9dfe2; --gold:#fbd98a; --coral:#e27b6b;
}
*{box-sizing:border-box;margin:0;padding:0}
html,body{width:1200px;height:3186px;overflow:hidden}
body{font-family:"Open Sans",Arial,sans-serif;color:var(--ink);background:#fff;position:relative}
.abs{position:absolute}
.stripe{left:0;top:0;width:1200px;height:8px;display:flex}
.stripe span{flex:1}
/* header */
.site-header{left:0;top:8px;width:1200px;height:77px;background:#fff}
.brand{left:120px;top:20px;display:flex;align-items:center;gap:10px;color:var(--blue);font-weight:700;font-size:17px;line-height:19px;letter-spacing:.3px}
.brand-square{width:40px;height:40px;background:var(--blue)}
.main-nav{left:455px;top:26px;display:flex;gap:0}
.main-nav a{font-size:16px;color:var(--ink);text-decoration:none;padding:0 11px 6px;font-weight:600}
.main-nav a.active{color:var(--teal);border-bottom:2px solid var(--teal)}
/* hero */
.hero{left:0;top:85px;width:1200px;height:592px;background:linear-gradient(100deg,#c98a2a 0%,#e7b768 25%,#f3dcc0 55%,#efe7e1 100%)}
.lang-switch{left:1004px;top:88px;width:86px;background:#fff;font-size:13px;text-align:center;padding:3px 0 5px;box-shadow:0 2px 6px rgba(0,0,0,.12)}
.lang-switch .current{font-size:16px;color:var(--ink)}
.lang-switch .opt{color:var(--teal)}
.lang-switch .opt.alt{color:var(--ink)}
.hero-tab{top:624px;width:226px;height:53px;border-radius:8px 8px 0 0;color:#fff;font-weight:700;font-size:15px;display:flex;align-items:center;padding-left:20px;gap:12px}
.hero-tab svg{width:30px;height:24px}
/* about */
.about{left:0;top:677px;width:1200px;height:889px;background:linear-gradient(180deg,#e9f8f9,#f2fbfb)}
.about-illus{left:0;top:876px;width:491px;height:531px;background:radial-gradient(ellipse at 55% 45%,#dbeefa 0%,#b7dcf0 45%,#eaf6fa 75%);border-radius:40% 40% 10% 10%}
.eyebrow{color:var(--teal);font-size:24px}
.about-title{left:504px;top:740px;font-size:28px;font-weight:700}
.about-copy{left:504px;top:791px;width:584px;font-size:13.5px;line-height:26px;color:var(--grey);text-align:justify}
.service-card{width:284px;height:266px;background:#fff;border:1px solid var(--line);padding:40px 14px 0 14px}
.service-card h3{font-size:24px;font-weight:400;line-height:29px;color:var(--ink);margin-bottom:14px}
.service-card p{font-size:14px;line-height:24px;color:var(--grey)}
.service-card .more{font-size:13.5px;font-weight:700;color:var(--ink);margin-top:12px;display:block}
.card-icon{width:92px;height:92px;border-radius:50%;background:var(--teal);border:4px solid #fff;display:flex;align-items:center;justify-content:center}
.wave{left:0;top:1520px;width:1200px;height:130px}
/* patient info */
.patient-btn{width:247px;height:93px;display:flex;align-items:center;gap:14px;padding-left:18px;color:#fff;font-weight:800;font-size:22px;line-height:27px;letter-spacing:.5px}
.patient-btn .ic{width:48px;height:48px;border:2px solid #fff;border-radius:6px;display:flex;align-items:center;justify-content:center;flex:none}
.connectors{left:0;top:1633px;width:1200px;height:460px}
.phone-illus{left:531px;top:1667px;width:186px;height:391px;border-radius:36px;background:linear-gradient(180deg,#dff1fb,#ffffff 40%,#cfe9f6);border:5px solid var(--blue-mid)}
.plan-box{left:778px;top:1784px;width:422px;height:274px;background:#fff;box-shadow:-4px 6px 18px rgba(0,0,0,.18);text-align:center;padding-top:8px}
.plan-box h2{font-size:54px;line-height:58px;font-weight:700;color:#000}
.plan-box .sub{font-size:19px;color:#bdbdbd;margin-top:8px}
.book-btn{display:inline-block;margin-top:18px;width:252px;height:61px;line-height:61px;background:var(--gold);color:#fff;font-weight:700;font-size:24px;letter-spacing:1px}
.lower-wave{left:0;top:2058px;width:1200px;height:56px}
/* discover */
.discover-eyebrow{left:109px;top:2117px;font-size:28px}
.discover-title{left:109px;top:2152px;font-size:32px;line-height:42px;font-weight:700}
.discover-copy{left:109px;top:2257px;width:409px;font-size:13px;line-height:23px;color:var(--grey)}
.appoint-btn{left:109px;top:2371px;width:252px;height:58px;background:var(--teal);color:#fff;font-weight:700;font-size:19px;display:flex;align-items:center;justify-content:center;letter-spacing:.5px}
.icon-grid{left:566px;top:2105px;width:522px;height:324px;background:#fff;box-shadow:0 4px 16px rgba(0,0,0,.15);display:grid;grid-template-columns:repeat(4,1fr);padding:40px 20px 0}
.icon-item{text-align:center;font-size:13.5px;color:var(--ink);height:130px}
.icon-item svg{width:56px;height:62px;display:block;margin:0 auto 8px}
/* video / how */
.video-band{left:0;top:2477px;width:1200px;height:390px;background:#a9ddd8}
.band-title{font-size:32px;font-weight:700;color:var(--ink)}
.video-thumb{left:111px;top:2575px;width:335px;height:260px;border-radius:10px;background:linear-gradient(135deg,#6fb9dc,#3d8dbd 60%,#9cd0ea)}
.play{left:210px;top:2638px;width:134px;height:134px;border-radius:50%;background:rgba(255,255,255,.85);display:flex;align-items:center;justify-content:center}
.play span{width:100px;height:100px;border-radius:50%;background:#000;display:flex;align-items:center;justify-content:center}
.faq-item{left:664px;width:419px;height:46px;border-radius:23px;display:flex;align-items:center;gap:24px;padding-left:10px;color:#fff;font-size:12px;font-weight:700}
.faq-item .dot{width:28px;height:28px;border-radius:50%;background:rgba(255,255,255,.25);display:flex;align-items:center;justify-content:center;font-size:20px}
.faq-answer{left:722px;top:2636px;width:360px;font-size:13px;line-height:22px;color:var(--ink)}
/* footer */
.site-footer{left:0;top:2867px;width:1200px;height:319px;background:var(--teal);color:#fff}
.footer-stripe{left:0;top:2867px;width:1200px;height:8px;display:flex}
.footer-stripe span{flex:1}
.footer-brand{left:111px;top:2899px;width:247px;height:61px;background:#fff;display:flex;align-items:center;gap:10px;padding-left:14px;color:var(--blue);font-weight:700;font-size:14px;line-height:17px}
.footer-brand .brand-square{width:32px;height:32px}
.footer-copy{left:111px;top:2983px;width:320px;font-size:13.5px;line-height:26px}
.footer-legal{left:111px;top:3157px;font-size:12px}
.footer-legal b{font-weight:700}
.footer-head{font-size:26px;font-weight:700}
.quick-links{left:611px;top:2958px;list-style:none;font-size:14px;line-height:29px}
.contact-line{left:838px;font-size:17px;display:flex;align-items:center;gap:10px}
.socials{left:868px;top:3108px;display:flex;gap:10px}
.socials span{width:46px;height:46px;border-radius:50%;border:2px solid #fff}
</style>
</head>
<body>

<div class="abs stripe">
  <span style="background:var(--teal)"></span><span style="background:var(--blue)"></span><span style="background:var(--teal-mid)"></span><span style="background:var(--blue-deep)"></span><span style="background:var(--blue-soft)"></span><span style="background:var(--teal)"></span>
</div>

<header class="abs site-header">
  <div class="abs brand"><span class="brand-square"></span><span>THE BRIGHT HARBOR<br>CLINIC</span></div>
  <nav class="abs main-nav">
    <a class="active" href="#">Home</a><a href="#">Meet us</a><a href="#">Services</a><a href="#">Patient Info</a><a href="#">Cases&amp;Reviews</a><a href="#">Blog</a><a href="#">Contact</a>
  </nav>
</header>

<section class="abs hero" role="img" aria-label="Smiling patient in a dental chair during a check-up"></section>
<div class="abs lang-switch"><div class="current">English &#8964;</div><div class="opt">English</div><div class="opt alt">Chinese</div></div>

<div class="abs hero-tab" style="left:173px;background:var(--blue-mid)">
  <svg viewBox="0 0 30 24" fill="none" stroke="#fff" stroke-width="2"><rect x="1" y="2" width="28" height="20" rx="3"/><path d="M6 12h18M10 8v8M20 8v8"/></svg>WHITENING</div>
<div class="abs hero-tab" style="left:486px;background:var(--teal-mid)">
  <svg viewBox="0 0 30 24" fill="none" stroke="#fff" stroke-width="2"><rect x="3" y="1" width="24" height="22" rx="2"/><path d="M9 8h12M9 13h12M9 18h8"/></svg>RADIOLOGY</div>
<div class="abs hero-tab" style="left:810px;background:var(--coral)">
  <svg viewBox="0 0 30 24" fill="none" stroke="#fff" stroke-width="2"><rect x="2" y="2" width="26" height="20" rx="2"/><path d="M15 6v12M11 9h8M11 13h8"/></svg>IMPLANTOLOGY</div>

<section class="abs about"></section>
<div class="abs about-illus" role="img" aria-label="Illustration of dentists inspecting a large tooth with a magnifying glass"></div>
<div class="abs eyebrow" style="left:504px;top:700px">About us</div>
<h1 class="abs about-title">What you should know</h1>
<p class="abs about-copy">Lorem Ipsum is simply dummy text of the printing and typesetting industry. Lorem Ipsum has been the industry's standard dummy text ever since the 1500s, when an unknown printer took a galley of type and scrambled it to make a type specimen book. It has survived not only five centuries.</p>

<article class="abs service-card" style="left:499px;top:942px"><h3>Cleaning and<br>Prevention</h3><p>Lorem Ipsum is simply dummy text of the printing and typeset-ting industry. Lorem Ipsum has been the industry's</p><a class="more">Read more &gt;</a></article>
<article class="abs service-card" style="left:810px;top:942px"><h3>Cosmetic<br>Dentistry</h3><p>Lorem Ipsum is simply dummy text of the printing and typeset-ting industry. Lorem Ipsum has been the industry's</p><a class="more">Read more &gt;</a></article>
<article class="abs service-card" style="left:499px;top:1269px"><h3>Implant<br>Dentistry</h3><p>Lorem Ipsum is simply dummy text of the printing and typeset-ting industry. Lorem Ipsum has been the industry's</p><a class="more">Read more &gt;</a></article>
<article class="abs service-card" style="left:810px;top:1269px"><h3>Removable<br>Dentures</h3><p>Lorem Ipsum is simply dummy text of the printing and typeset-ting industry. Lorem Ipsum has been the industry's</p><a class="more">Read more &gt;</a></article>

<svg width="0" height="0" style="position:absolute">
  <defs>
    <symbol id="tooth" viewBox="0 0 40 44"><path d="M8 4c5-3 9 1 12 1s7-4 12-1c5 4 3 13 1 18-2 6-2 20-6 20-4 0-3-12-7-12s-3 12-7 12c-4 0-4-14-6-20C5 17 3 8 8 4z" fill="none" stroke="currentColor" stroke-width="2.4" stroke-linejoin="round"/></symbol>
  </defs>
</svg>

<div class="abs card-icon" style="left:675px;top:900px"><svg width="46" height="46" viewBox="0 0 40 40" fill="none" stroke="#fff" stroke-width="2.5"><path d="M20 6a14 14 0 1 1-13 9M7 6v9h9"/></svg></div>
<div class="abs card-icon" style="left:982px;top:900px;color:#fff"><svg width="46" height="50"><use href="#tooth"/></svg></div>
<div class="abs card-icon" style="left:675px;top:1227px"><svg width="40" height="50" viewBox="0 0 40 50" fill="none" stroke="#fff" stroke-width="2.5"><path d="M8 6c6-4 18-4 24 0-1 8-6 12-12 12S9 14 8 6zM14 22h12M14 28h12M15 34h10M17 40h6"/></svg></div>
<div class="abs card-icon" style="left:982px;top:1227px"><svg width="56" height="30" viewBox="0 0 56 30" fill="none" stroke="#fff" stroke-width="2.5"><rect x="2" y="6" width="52" height="18" rx="9"/><path d="M14 8v14M24 8v14M34 8v14M44 8v14"/></svg></div>

<svg class="abs wave" viewBox="0 0 1200 130" preserveAspectRatio="none">
  <path d="M0 46h1200v84H0z" fill="#fff"/>
  <path d="M0 55C250 15 420 95 640 70 860 45 1000 20 1200 60V80C1000 45 860 80 640 95 420 115 250 40 0 80z" fill="var(--teal-soft)"/>
  <path d="M0 70C260 40 440 110 650 85 860 62 1010 45 1200 75V88C1010 65 860 95 650 108 430 125 260 60 0 92z" fill="var(--teal-mid)" opacity=".6"/>
</svg>

<svg class="abs connectors" viewBox="0 0 1200 460" fill="none" stroke="#e1e4e6" stroke-width="10" stroke-linecap="round">
  <path d="M353 60C420 40 470 50 530 90"/><path d="M438 190C480 180 500 175 530 170"/><path d="M353 325C420 330 480 300 530 270"/><path d="M836 60C780 30 740 40 717 80"/>
</svg>

<div class="abs patient-btn" style="left:106px;top:1646px;background:var(--blue-mid)"><span class="ic" style="font-size:20px">%</span>NEW PATIENT<br>OFFER</div>
<div class="abs patient-btn" style="left:191px;top:1779px;background:var(--teal-pale)"><span class="ic"><svg width="28" height="28" viewBox="0 0 28 28" fill="none" stroke="#fff" stroke-width="2"><path d="M2 14a12 12 0 0 1 24 0zM14 14v9a3 3 0 0 1-6 0"/></svg></span>ACCEPTED<br>INSURANCE</div>
<div class="abs patient-btn" style="left:106px;top:1912px;background:var(--teal)"><span class="ic"><svg width="28" height="28" viewBox="0 0 28 28" fill="none" stroke="#fff" stroke-width="2"><circle cx="14" cy="10" r="5"/><path d="M4 26c0-6 4-9 10-9s10 3 10 9"/></svg></span>PATIENT<br>PORTAL</div>
<div class="abs patient-btn" style="left:836px;top:1646px;background:var(--blue-deep)"><span class="ic"><svg width="24" height="28" viewBox="0 0 24 28" fill="none" stroke="#fff" stroke-width="2"><path d="M3 2h18v24H3zM7 8h10M7 13h10M7 18h6"/></svg></span>SPECIAL<br>HELPFUL TIPS</div>

<div class="abs phone-illus" role="img" aria-label="Illustration of a smartphone showing the clinic app under a cloud"></div>

<div class="abs plan-box">
  <h2>Plan Your<br>Visit Now</h2>
  <div class="sub">Begin the Change</div>
  <a class="book-btn">BOOK NOW</a>
</div>

<svg class="abs lower-wave" viewBox="0 0 1200 56" preserveAspectRatio="none"><path d="M0 20C300 50 700 0 1200 25V56H0z" fill="var(--teal-pale)" opacity=".7"/><path d="M0 40C350 60 750 20 1200 42V56H0z" fill="#fff"/></svg>

<div class="abs discover-eyebrow">Discover</div>
<h2 class="abs discover-title">Dental Office - The Bright<br>Harbor Clinic</h2>
<p class="abs discover-copy">Lorem Ipsum is simply dummy text of the printing and typeset-ting industry. Lorem Ipsum has been the industry's standard dummy text ever since the 1500s, when an unknown printer took a galley of type and scrambled it to make a type specimen book.</p>
<a class="abs appoint-btn">MAKE APPOINMENT</a>

<div class="abs icon-grid" style="color:var(--blue)">
  <div class="icon-item"><svg><use href="#tooth"/></svg>IMPLANTS</div>
  <div class="icon-item"><svg><use href="#tooth"/></svg>GUM</div>
  <div class="icon-item"><svg><use href="#tooth"/></svg>ROOTS</div>
  <div class="icon-item"><svg viewBox="0 0 56 62" fill="none" stroke="currentColor" stroke-width="2.4"><rect x="6" y="8" width="44" height="46" rx="3"/><path d="M18 22l20 20M38 22L18 42"/></svg>X-RAY</div>
  <div class="icon-item"><svg><use href="#tooth"/></svg>WHITENING</div>
  <div class="icon-item"><svg><use href="#tooth"/></svg>PREVENTION</div>
  <div class="icon-item"><svg><use href="#tooth"/></svg>CARIES</div>
  <div class="icon-item"><svg viewBox="0 0 56 62" fill="none" stroke="currentColor" stroke-width="2.4"><rect x="8" y="6" width="40" height="50" rx="3"/><path d="M16 20h24M16 30h24M16 40h16"/></svg>iDOCTOR</div>
</div>

<section class="abs video-band"></section>
<h2 class="abs band-title" style="left:117px;top:2500px">Our Video</h2>
<h2 class="abs band-title" style="left:664px;top:2500px">How it works</h2>
<div class="abs video-thumb" role="img" aria-label="Video still of a dentist treating a patient"></div>
<div class="abs play"><span><svg width="40" height="44" viewBox="0 0 40 44"><path d="M6 4l30 18L6 40z" fill="#fff"/></svg></span></div>

<div class="abs faq-item" style="top:2575px;background:var(--teal)"><span class="dot">+</span>WHAT METHOD DO YOU USE FOR CLEANING?</div>
<p class="abs faq-answer">Lorem Ipsum is simply dummy text of the printing and typesetting industry. Lorem Ipsum has been the industry's standard dummy text ever since the 1500s.</p>
<div class="abs faq-item" style="top:2724px;background:var(--blue-soft)"><span class="dot">+</span>WHAT METHOD DO YOU USE FOR CLEANING?</div>
<div class="abs faq-item" style="top:2785px;background:var(--blue-soft)"><span class="dot">+</span>WHAT METHOD DO YOU USE FOR CLEANING?</div>

<footer class="abs site-footer"></footer>
<div class="abs footer-stripe">
  <span style="background:var(--teal-mid)"></span><span style="background:var(--blue)"></span><span style="background:var(--blue-deep)"></span><span style="background:var(--teal-soft)"></span><span style="background:var(--blue-mid)"></span><span style="background:#333"></span>
</div>
<div class="abs footer-brand"><span class="brand-square"></span><span>THE BRIGHT HARBOR<br>CLINIC</span></div>
<p class="abs footer-copy" style="color:#fff">Lorem Ipsum is simply dummy text of the print-ing and typesetting industry. Lorem Ipsum has been the industry's standard dummy text ever since the 1500s, when an unknown printer took a galley of type and scrambled it to make a type specimen book.</p>
<div class="abs footer-legal" style="color:#fff"><b>THE BRIGHT HARBOR CLINIC</b> © 2019. All rights reserved.</div>

<h3 class="abs footer-head" style="left:611px;top:2905px;color:#fff">Quick links</h3>
<ul class="abs quick-links" style="color:#fff"><li>Home</li><li>Meet us</li><li>Services</li><li>Patient Info</li><li>Cases &amp; Reviews</li><li>Blog</li><li>Contact</li></ul>

<h3 class="abs footer-head" style="left:868px;top:2905px;color:#fff">Contact Us</h3>
<div class="abs contact-line" style="top:2966px;color:#fff"><svg width="26" height="26" viewBox="0 0 26 26" fill="none" stroke="#fff" stroke-width="2"><circle cx="13" cy="13" r="11"/><path d="M9 7l3 3-2 2c1 2 2 3 4 4l2-2 3 3-2 2c-5 0-10-5-10-10z"/></svg>0001-5550-0142</div>
<div class="abs contact-line" style="top:3008px;font-size:14px;color:#fff"><svg width="26" height="20" viewBox="0 0 26 20" fill="none" stroke="#fff" stroke-width="2"><rect x="1" y="1" width="24" height="18"/><path d="M1 1l12 10L25 1"/></svg>support@thebrightharborclinic.example</div>
<h3 class="abs footer-head" style="left:877px;top:3055px;color:#fff">Follow Us</h3>
<div class="abs socials" aria-label="Social media links"><span></span><span></span><span></span></div>

</body>
</html>
```